pharmacy/travel clinic business card design

We need a business card for our new business called Brenwick Travel Clinic and Pharmacy. Our primary focus is doing consultations for people before travelling internationally and providing vaccinations and prescriptions for them. While the business is considered a pharmacy, it has more the look and feel of a doctor's office. The design should communicate a professional and trustworthy feel. I have attached a copy of the logo we are going to be using.
Updates
Thanks for the submissions.  If you haven`t been eliminated you are one of the finalists.  Decision will likely be made tomorrow.

Target Market(s)
Customers, other health care professionals, travel agents
Industry/Entity Type
Clinic
Look and feel
Each slider illustrates characteristics of the customer's brand and the style your logo design should communicate.

```html
<!DOCTYPE html>
<html lang="en">
<head>
<meta charset="utf-8">
<title>Brenwick Travel Clinic and Pharmacy – Business Card</title>
<link rel="stylesheet" href="https://fonts.googleapis.com/css2?family=Arimo:wght@400;700&display=swap">
<style>
  :root {
    --paper: #ffffff;
    --paper-shade: #e9e9ea;
    --brand-blue: #2b8fd8;
    --divider-blue: #2a86cf;
    --band-edge: #1d2f6e;
    --band-deep: #1c3f86;
    --band-mid: #1689c9;
    --band-glow: #8fd3f2;
    --band-right: #1f3d6b;
  }
  * { margin: 0; padding: 0; box-sizing: border-box; }
  html, body {
    width: 1200px;
    height: 800px;
    overflow: hidden;
    background: var(--paper);
  }
  .card {
    position: relative;
    width: 1200px;
    height: 800px;
    overflow: hidden;
    font-family: "Arimo", Arial, sans-serif;
    background:
      radial-gradient(ellipse 620px 300px at 640px 60px, var(--paper) 35%, transparent 100%),
      radial-gradient(ellipse 900px 420px at 600px 220px, var(--paper) 40%, var(--paper-shade) 100%);
  }
  .brand {
    position: absolute;
    left: 70px;
    top: 170px;
    display: flex;
    align-items: flex-start;
    gap: 16px;
    color: var(--brand-blue);
    font-weight: 700;
  }
  .brand-dot {
    width: 30px;
    height: 30px;
    margin-top: 14px;
    border-radius: 50%;
    background: var(--brand-blue);
    flex: none;
  }
  .brand-name {
    line-height: 1;
  }
  .brand-name .line-primary { display: block; font-size: 58px; letter-spacing: -1px; }
  .brand-name .line-secondary { display: block; font-size: 58px; letter-spacing: -1px; margin-top: 4px; }
  .brand-name .line-tertiary { display: block; font-size: 24px; margin-top: 8px; letter-spacing: 0.5px; }
  .divider {
    position: absolute;
    left: 578px;
    top: 125px;
    width: 3px;
    height: 250px;
    background: var(--divider-blue);
  }
  .contact {
    position: absolute;
    left: 605px;
    top: 188px;
    list-style: none;
    color: var(--brand-blue);
    font-size: 32px;
    line-height: 33px;
  }
  .band {
    position: absolute;
    left: 0;
    top: 450px;
    width: 1200px;
    height: 350px;
    border-top: 6px solid var(--band-edge);
    background:
      radial-gradient(ellipse 90px 300px at 565px 0, var(--band-glow) 0%, rgba(143,211,242,0.35) 45%, transparent 100%),
      linear-gradient(90deg, var(--band-deep) 0%, var(--band-mid) 30%, var(--band-mid) 55%, var(--band-right) 100%);
  }
  .band::after {
    content: "";
    position: absolute;
    inset: 0;
    background: linear-gradient(180deg, rgba(255,255,255,0.12) 0%, rgba(0,0,0,0.15) 100%);
  }
</style>
</head>
<body>
  <main class="card">
    <div class="brand">
      <span class="brand-dot"></span>
      <div class="brand-name">
        <span class="line-primary">Brenwick</span>
        <span class="line-secondary">Travel Clinic</span>
        <span class="line-tertiary">and Pharmacy</span>
      </div>
    </div>

    <div class="divider"></div>

    <ul class="contact">
      <li>Tel: 000-000-0000</li>
      <li>Fax: 000-000-0000</li>
      <li>Email: contactus@brenwickclinic.com</li>
      <li>Address: Bienvenue a note company</li>
    </ul>

    <div class="band"></div>
  </main>
</body>
</html>
```